Catering Box for Food

We run a restaurant business called "Brill3Way"
www.brill3way.com
We're expanding into catering services and are currently designing a new delivery box.
---Box Concept
The food will be packed in a full-size aluminum tray.
The tray will be placed inside a white paper box for delivery and branding purposes.(as the pics showed )
Box dimensions: 21 x 13 x 4 inches
Brand color: HEX #FF6C0E
The design should use no more than two colors (not including white).
---Design Requirements Please create a design for all five visible surfaces of the box:
Top
Front
Back
Left side
Right side
---Additional Info
The box should also include our store locations, with addresses and phone numbers clearly displayed.

```html
<!DOCTYPE html>
<html lang="en">
<head>
<meta charset="utf-8">
<title>Brill3Way Catering Box</title>
<link rel="stylesheet" href="https://fonts.googleapis.com/css2?family=Archivo+Black&family=Montserrat:wght@500;700;800&family=Roboto+Condensed:ital,wght@1,800&display=swap">
<style>
  :root {
    --brand-orange: #DC6630;
    --checker-tint: #EBA27E;
    --box-white: #F1F2F5;
    --ink: #1F2228;
    --ink-soft: #55585E;
    --backdrop: #D9D9DB;
  }
  * { margin: 0; padding: 0; box-sizing: border-box; }
  html, body { width: 1200px; height: 902px; overflow: hidden; }
  body { background: var(--backdrop); position: relative; font-family: "Montserrat", sans-serif; }

  .panel { position: absolute; background: var(--box-white); overflow: hidden; box-shadow: 0 2px 6px rgba(0,0,0,.12); }
  .checker-area { position: absolute; background: linear-gradient(135deg, var(--brand-orange), var(--checker-tint)); }

  /* Top lid 21 x 13 in */
  .lid { left: 44px; top: 167px; width: 672px; height: 416px; }
  .lid .checker-left { left: 0; top: 0; width: 52px; height: 100%; }
  .lid .checker-right { right: 0; top: 0; width: 52px; height: 100%; }
  .lid-brand { position: absolute; left: 0; right: 0; top: 96px; text-align: center; }
  .lid-name { font-family: "Archivo Black", sans-serif; font-size: 78px; line-height: 1; color: var(--brand-orange); letter-spacing: 1px; }
  .lid-cuisine { font-family: "Archivo Black", sans-serif; font-size: 22px; color: var(--brand-orange); letter-spacing: 3px; margin-top: 10px; }
  .lid-rule { width: 240px; height: 10px; margin: 12px auto 0; background: var(--brand-orange); opacity: .75; }
  .catering-bar { width: 420px; margin: 16px auto 0; background: var(--brand-orange); color: #fff; font-family: "Archivo Black", sans-serif; font-size: 34px; letter-spacing: 3px; padding: 6px 0; }

  /* Front side 21 x 4 in */
  .front { left: 44px; top: 607px; width: 672px; height: 128px; }
  .front .checker-end { left: 0; top: 0; width: 40px; height: 100%; }
  .front-brand { position: absolute; left: 60px; top: 18px; font-family: "Archivo Black", sans-serif; font-size: 22px; color: var(--brand-orange); }
  .front-divider { position: absolute; left: 190px; top: 16px; width: 2px; height: 40px; background: var(--brand-orange); }
  .front-heading { position: absolute; left: 204px; top: 14px; font-weight: 800; font-size: 19px; line-height: 1.05; color: var(--ink); }
  .branch { position: absolute; display: flex; gap: 10px; align-items: flex-start; }
  .branch-downtown { left: 60px; top: 72px; }
  .branch-uptown { left: 330px; top: 72px; }
  .branch-name { font-weight: 700; font-size: 11px; line-height: 1.15; color: var(--ink); }
  .branch-info { font-weight: 500; font-size: 9.5px; line-height: 1.3; color: var(--ink-soft); }
  .pin { width: 11px; height: 15px; flex: none; }
  .front-web { position: absolute; right: 18px; bottom: 10px; font-family: "Roboto Condensed", sans-serif; font-style: italic; font-weight: 800; font-size: 14px; color: var(--brand-orange); }

  /* Right side 13 x 4 in */
  .side { left: 740px; top: 607px; width: 416px; height: 128px; }
  .side .checker-frame { inset: 0; }
  .side-window { position: absolute; left: 44px; right: 44px; top: 26px; bottom: 26px; background: var(--box-white); display: flex; align-items: center; justify-content: center; }
  .tagline { font-family: "Roboto Condensed", sans-serif; font-style: italic; font-weight: 800; font-size: 24px; color: var(--brand-orange); }
</style>
</head>
<body>

<section class="panel lid">
  <div class="checker-area checker-left" role="img" aria-label="Orange and white checkerboard band"></div>
  <div class="checker-area checker-right" role="img" aria-label="Orange and white checkerboard band"></div>
  <div class="lid-brand">
    <div class="lid-name">Brill3Way</div>
    <div class="lid-cuisine">HAINAN CHICKEN</div>
    <div class="lid-rule"></div>
    <div class="catering-bar">CATERING</div>
  </div>
</section>

<section class="panel front">
  <div class="checker-area checker-end" role="img" aria-label="Orange and white checkerboard band"></div>
  <div class="front-brand">Brill3Way</div>
  <div class="front-divider"></div>
  <div class="front-heading">OUR<br>LOCATION</div>

  <div class="branch branch-downtown">
    <svg class="pin" viewBox="0 0 12 16"><path d="M6 0a6 6 0 0 0-6 6c0 4.5 6 10 6 10s6-5.5 6-10a6 6 0 0 0-6-6zm0 8.5A2.5 2.5 0 1 1 6 3.5a2.5 2.5 0 0 1 0 5z" fill="var(--brand-orange)"/></svg>
    <div class="branch-name">DOWNTOWN<br>BRANCH</div>
    <div class="branch-info">123 MAIN STREET, CITY<br>(123) 456-7890</div>
  </div>

  <div class="branch branch-uptown">
    <svg class="pin" viewBox="0 0 12 16"><path d="M6 0a6 6 0 0 0-6 6c0 4.5 6 10 6 10s6-5.5 6-10a6 6 0 0 0-6-6zm0 8.5A2.5 2.5 0 1 1 6 3.5a2.5 2.5 0 0 1 0 5z" fill="var(--brand-orange)"/></svg>
    <div class="branch-name">UPTOWN<br>BRANCH</div>
    <div class="branch-info">123 MAIN STREET, CITY<br>(123) 456-7890</div>
  </div>

  <div class="front-web">www.brill3way.com</div>
</section>

<section class="panel side">
  <div class="checker-area checker-frame" role="img" aria-label="Orange and white checkerboard frame"></div>
  <div class="side-window">
    <span class="tagline">Fresh, Hot &amp; Ready to Share</span>
  </div>
</section>

</body>
</html>
```